Business Card Design

New business card design

Target Market(s)

Residential & Commercial Property Managers

Industry/Entity Type

Plumbing Services

Contact Information for Business Card

Name - Owen Tredgold, title - Director, Phone Number - 0431 862 507, email - owen@rvb-plumbing.com.au, Company ABN - 73 215 904 386,

Font styles to use
Sans Serif

Colors
0054AA
0677BA
7BADD7
CADEEF
E8F1F8

```html
<!DOCTYPE html>
<html lang="en">
<head>
<meta charset="utf-8">
<title>RVB Plumbing Services – Business Card</title>
<link rel="stylesheet" href="https://fonts.googleapis.com/css2?family=Montserrat:wght@400;700&display=swap">
<style>
  :root {
    --backdrop: #b9b8b3;
    --card-white: #ffffff;
    --card-dark: #1c232b;
    --brand-deep: #0054AA;
    --brand-blue: #0677BA;
    --brand-sky: #7BADD7;
    --brand-mist: #CADEEF;
    --brand-ice: #E8F1F8;
    --ink: #1e2329;
    --ink-soft: #2b3138;
    --logo-light: #ffffff;
  }
  * { margin: 0; padding: 0; box-sizing: border-box; }
  html, body {
    width: 1200px; height: 857px; overflow: hidden;
    background: var(--backdrop);
    font-family: "Montserrat", Arial, sans-serif;
  }
  .stage {
    width: 1200px; height: 857px;
    display: flex; align-items: center; justify-content: center; gap: 40px;
  }
  .card {
    position: relative;
    width: 540px; height: 309px;
    border-bottom: 4px solid var(--brand-blue);
    box-shadow: 0 14px 30px rgba(0,0,0,0.22);
    overflow: hidden;
  }
  .card--front { background: var(--card-white); }
  .card--back { background: var(--card-dark); }

  .brand {
    position: absolute;
    display: flex; align-items: center; gap: 10px;
    white-space: nowrap;
    font-weight: 400; letter-spacing: 0.3px;
  }
  .brand__dot { width: 11px; height: 11px; border-radius: 50%; flex: none; }
  .brand__name { font-size: 18px; }
  .card--front .brand { left: 32px; top: 138px; color: var(--ink); }
  .card--front .brand__dot { background: var(--brand-blue); }
  .card--back .brand {
    left: 50%; top: 50%; transform: translate(-50%, -50%);
    color: var(--logo-light);
  }
  .card--back .brand__name { font-size: 28px; }
  .card--back .brand__dot { width: 14px; height: 14px; background: var(--brand-sky); }

  .divider {
    position: absolute; left: 282px; top: 178px; bottom: 0;
    width: 1.5px; background: var(--brand-blue);
  }
  .contact { position: absolute; left: 300px; top: 54px; color: var(--ink-soft); }
  .contact__name {
    color: var(--brand-blue); font-weight: 700; font-size: 19px; letter-spacing: 0.5px;
  }
  .contact__title { font-size: 15px; margin-top: 2px; color: var(--brand-deep); }
  .contact__list { list-style: none; margin-top: 20px; }
  .contact__item {
    display: flex; align-items: center; gap: 10px;
    font-size: 14px; line-height: 25px; white-space: nowrap;
  }
  .contact__icon { width: 14px; height: 14px; flex: none; }
  .contact__label {
    width: 14px; flex: none; font-size: 8px; font-weight: 700;
    color: var(--brand-blue); letter-spacing: -0.3px;
  }
</style>
</head>
<body>
<main class="stage">
  <section class="card card--front" aria-label="Business card front">
    <div class="brand">
      <span class="brand__name">rvb plumbing services</span>
      <span class="brand__dot"></span>
    </div>
    <div class="divider"></div>
    <div class="contact">
      <p class="contact__name">OWEN TREDGOLD</p>
      <p class="contact__title">Director</p>
      <ul class="contact__list">
        <li class="contact__item">
          <svg class="contact__icon" viewBox="0 0 16 16"><path fill="var(--brand-blue)" d="M4.2 1.5l2 3-1.3 1.4c.8 1.8 2 3 3.8 3.9l1.4-1.3 3 2-1 2.7C6.8 13.2 2.8 9.2 1.5 2.5z"/></svg>
          <span>0431 862 507</span>
        </li>
        <li class="contact__item">
          <svg class="contact__icon" viewBox="0 0 16 16"><rect x="1" y="3" width="14" height="10" fill="var(--brand-blue)"/><path d="M1 3l7 6 7-6" fill="none" stroke="#fff" stroke-width="1.2"/></svg>
          <span>owen@rvb-plumbing.com.au</span>
        </li>
        <li class="contact__item">
          <svg class="contact__icon" viewBox="0 0 16 16" fill="none" stroke="var(--brand-blue)" stroke-width="1.3"><circle cx="8" cy="8" r="6.5"/><ellipse cx="8" cy="8" rx="3" ry="6.5"/><path d="M1.5 8h13"/></svg>
          <span>rvb-plumbing.com.au</span>
        </li>
        <li class="contact__item">
          <span class="contact__label">ABN</span>
          <span>73 215 904 386</span>
        </li>
      </ul>
    </div>
  </section>

  <section class="card card--back" aria-label="Business card back">
    <div class="brand">
      <span class="brand__name">rvb plumbing services</span>
      <span class="brand__dot"></span>
    </div>
  </section>
</main>
</body>
</html>
```